Harbor & Quillstone executive recruiting services

I started a plankfold website using an existing template and some of the original content is still on this UNpublished work in progress. I am an executive recruiter offering services to both Clients and Candidates in many sectors and using creative sourcing methodologies. I have 30+ years of business experience combined with my recruiting experience. I like the color teal and used it for the site I started. The tabs should be
About (me)
Services (for Clients and Candidates)
Industry Coverage
Recruiting Process (see attached flow chart)
Retained Agreement (see attached)
Personal Commitment
Testimonials
Content/articles/blogs etc
Contact
Updates

TO ALL DESIGNERS:
I have been granted a short extension to choose a design. Please resubmit designs using a new name DROVE EXECUTIVE SEARCH. Pls feel free to alert me with any questions and of course, when the edits are made.

thank you

Colette

Target Market(s)

Executives from Director, VP, SVP and C-Suite

Industry/Entity Type

recruiting industry for finance, Human Resoures, Sales/Marketing, Innovation/Transformation , Information Technology, Entertainment/Media/Telecommunications, Healthcare/Life Sciences,HCIT/Biotech

Font styles to use
Sans Serif

Colors
0094D4
00A9DD
6FCCEA
C7EBF8
E9F6FB

Requirements
Must have
• way to contact me - add calendar sign up
Nice to have
• process flow for the recruiting process (see attached)
Should not have
• guarantees

```html
<!DOCTYPE html>
<html lang="en">
<head>
<meta charset="utf-8">
<title>Harbor &amp; Quillstone — Executive Search</title>
<link href="https://fonts.googleapis.com/css2?family=Quicksand:wght@500;600&display=swap" rel="stylesheet">
<style>
  :root {
    --backdrop: #000000;
    --brand-blue: #1aafe1;
    --ink-light: #ffffff;
    --photo-base: #e4e7ea;
    --photo-shade: #cfd4d9;
    --token-red: #d23a4c;
    --token-green: #4e9e4a;
    --token-blue: #4a88b0;
    --token-yellow: #d8c546;
  }
  html, body {
    margin: 0;
    padding: 0;
    width: 1200px;
    height: 1200px;
    overflow: hidden;
    background: var(--backdrop);
    font-family: "Quicksand", sans-serif;
  }
  .site-home {
    position: absolute;
    left: 65px;
    top: 184px;
    width: 1072px;
    height: 832px;
    overflow: hidden;
    background: var(--photo-base);
  }
  .hero-photo {
    position: absolute;
    inset: 0;
    background:
      radial-gradient(ellipse 40% 35% at 72% 62%, rgba(78,158,74,0.45), transparent 70%),
      radial-gradient(ellipse 30% 30% at 60% 55%, rgba(210,58,76,0.35), transparent 70%),
      radial-gradient(ellipse 30% 30% at 82% 45%, rgba(74,136,176,0.35), transparent 70%),
      radial-gradient(ellipse 25% 25% at 68% 70%, rgba(216,197,70,0.3), transparent 70%),
      linear-gradient(160deg, #eef0f2 0%, var(--photo-base) 55%, var(--photo-shade) 100%);
  }
  .brand-panel {
    position: absolute;
    inset: 0;
    width: 1072px;
    height: 832px;
  }
  .brand-panel path { fill: var(--brand-blue); }
  .brand-mark {
    position: absolute;
    left: 56px;
    top: 40px;
    display: flex;
    align-items: center;
    gap: 14px;
    color: var(--ink-light);
  }
  .brand-mark__circle {
    width: 84px;
    height: 84px;
    border: 1.5px solid var(--ink-light);
    border-radius: 50%;
    box-sizing: border-box;
  }
  .brand-mark__name {
    font-size: 20px;
    font-weight: 500;
    letter-spacing: 0.3px;
  }
  .main-nav {
    position: absolute;
    left: 57px;
    top: 172px;
    margin: 0;
    padding: 0;
    list-style: none;
  }
  .main-nav li {
    height: 70.7px;
    font-size: 24px;
    font-weight: 500;
    color: var(--ink-light);
    letter-spacing: 0.2px;
    line-height: 34px;
  }
</style>
</head>
<body>
  <main class="site-home">
    <div class="hero-photo" role="img" aria-label="Photo of many colourful wooden game pawns in red, green, blue and yellow grouped on a pale grey surface"></div>
    <svg class="brand-panel" viewBox="0 0 1072 832" aria-hidden="true">
      <path d="M0 0 H412 C 362 80, 334 190, 340 300 C 350 500, 500 740, 679 832 H0 Z"/>
    </svg>
    <div class="brand-mark">
      <span class="brand-mark__circle"></span>
      <span class="brand-mark__name">Harbor &amp; Quillstone</span>
    </div>
    <ul class="main-nav">
      <li>About</li>
      <li>Services</li>
      <li>Industry Coverage</li>
      <li>Recruiting Process</li>
      <li>Retained Agreement</li>
      <li>Personal Commitment</li>
      <li>Testimonials</li>
      <li>Content/articles/blogs etc</li>
      <li>Contact</li>
    </ul>
  </main>
</body>
</html>
```